Book Cover for Cyber Compliance Book

I need to get a book cover designed for use on "Pagewell Print Portal" - template attached.

The name of the book is: Charting KELMOR

Tagline: A Boardroom Leader’s Field Guide to Oversight and Endurance

Author: Martin J Hollis

Photo of author is attached and a logo for the QBWLN publishing organisation.

Please note: the author is high profile in the cyber security industry and use of his image and name on the book will help online sales.

I am open to changing the amount of copy used on the front and back of the book.

The book is about a European regulation for the financial sector called DORA Digital Operational Resilience Act. It is aimed at corporate level executives within the financial sector and the imagery should include relevant elements such as the EU, Financial sector, digital operations and cybersecurity.

I want to find an imaginative designer than can create something special and appealing.

I am not clear on exactly how many pages will be in the book so the template details may change slightly as the number becomes clear for the width of the spine etc. I will require all the template files used so I can make minor edits in AI or Photoshop

Note I can get the photo and attached logo in higher resolution if required

If possible I would like to see a 3D mockup of the book

Synopsis of Book:

n the ever-evolving landscape of financial services, the Digital Operational Resilience Act (DORA) stands as a beacon of change, ushering in a new era of regulatory requirements aimed at fortifying the digital fortitude of the sector. “Charting KELMOR: A Boardroom Leader’s Field Guide to Oversight and Endurance” is an indispensable guide tailored for leaders who are steering their organisations through the complexities of DORA compliance.
This comprehensive manual delves into the intricacies of DORA, elucidating the rationale behind its inception – the need for a unified and robust approach to managing ICT risks that have become increasingly prevalent in today’s interconnected financial ecosystem. The book offers a granular analysis of the five pillars central to DORA: ICT Risk Management, ICT-related Incident Management, Digital Operational Resilience Testing, ICT Third Party Risk Management, and Information Sharing Arrangements.
For financial entities and ICT service providers operating within the EU and beyond, “Charting KELMOR” serves as a strategic compass. It provides actionable insights into aligning with DORA’s standards, ensuring not just compliance but also a competitive edge in the EU market. The guide highlights the strategic importance of continuous learning and the emergence of specialized roles such as DORA Compliance Specialists, addressing the skills gap and career opportunities within this new regulatory framework.
The book also offers a detailed walkthrough of the Union-wide Oversight Framework, a novel aspect of DORA that places critical ICT third-party providers under direct regulatory scrutiny. It outlines the necessary steps for financial entities to ensure seamless collaboration with these providers, including the integration of specific contractual obligations to uphold DORA’s stringent resilience standards.
With practical advice and real-world scenarios, “Charting KELMOR” equips executives with the knowledge to conduct thorough DORA Compliance Assessments, map dependencies, and engage in scenario testing that aligns with the act’s rigorous testing regimen. It is not just a guide but a strategic tool for proactive adaptation and evolution in the face of DORA’s demands.
As the financial sector navigates these new regulatory waters, “Charting KELMOR” emerges as the quintessential guide for those committed to not just surviving but thriving in the age of digital operational resilience. It is a clarion call for attentiveness, alignment, and preparedness – a must-read for every financial service executive determined to lead their organization with foresight and fortitude.

```html
<!DOCTYPE html>
<html lang="en">
<head>
<meta charset="utf-8">
<title>Charting KELMOR – Book Cover</title>
<link rel="stylesheet" href="https://fonts.googleapis.com/css2?family=Montserrat:wght@700;800&family=Jost:wght@400;500&display=swap">
<style>
  :root {
    --stage: #000000;
    --sky-top: #cfe6f7;
    --sky-mid: #8fcbef;
    --paper: #ffffff;
    --title-red: #d6432a;
    --title-navy: #1d3f93;
    --ink: #111111;
    --band-blue: #1c67a9;
    --chart-line: rgba(255,255,255,0.75);
    --chart-bar: rgba(255,255,255,0.45);
    --skin: #e2b79a;
    --suit: #222a3b;
  }
  * { margin: 0; padding: 0; box-sizing: border-box; }
  html, body { width: 1200px; height: 1200px; overflow: hidden; background: var(--stage); }
  .canvas { position: relative; width: 1200px; height: 1200px; background: var(--stage); }

  .cover {
    position: absolute; left: 360px; top: 240px; width: 480px; height: 720px; overflow: hidden;
    background: linear-gradient(180deg, var(--sky-top) 0%, #b6dcf3 30%, var(--sky-mid) 55%, #d8eefa 80%, var(--paper) 89%, var(--paper) 100%);
  }
  .cover__glow {
    position: absolute; inset: 0;
    background: radial-gradient(ellipse 60% 45% at 85% 50%, rgba(79,176,230,0.55), transparent 70%);
  }
  .cover__chart, .cover__portrait { position: absolute; left: 0; top: 0; width: 480px; height: 720px; }

  .cover__compass {
    position: absolute; left: 295px; top: -70px; width: 190px; height: 190px; border-radius: 50%;
    background: radial-gradient(circle, rgba(120,170,200,0.3) 0%, rgba(90,150,190,0.4) 60%, rgba(70,120,160,0.5) 100%);
    border: 3px solid rgba(90,140,175,0.45);
  }

  .cover__title {
    position: absolute; left: 0; right: 0; top: 100px;
    font-family: "Montserrat", sans-serif; font-weight: 800; line-height: 1;
  }
  .cover__title-lead { display: block; text-align: center; color: var(--title-red); font-size: 84px; letter-spacing: -0.5px; }
  .cover__title-main { display: block; text-align: right; padding-right: 16px; color: var(--title-navy); font-size: 70px; margin-top: 20px; }

  .cover__tagline {
    position: absolute; left: 210px; top: 378px; width: 265px;
    font-family: "Jost", sans-serif; font-weight: 400; font-size: 22px; line-height: 31px; color: var(--ink);
  }

  .cover__author {
    position: absolute; left: 227px; top: 591px; width: 253px; height: 52px;
    background: var(--band-blue); color: var(--paper);
    font-family: "Montserrat", sans-serif; font-weight: 700; font-size: 25px;
    display: flex; align-items: center; padding-left: 30px;
  }
</style>
</head>
<body>
<div class="canvas">
  <section class="cover">
    <div class="cover__glow"></div>

    <svg class="cover__chart" viewBox="0 0 480 720" aria-hidden="true">
      <g fill="var(--chart-bar)">
        <rect x="250" y="540" width="14" height="110"/>
        <rect x="272" y="500" width="14" height="150"/>
        <rect x="294" y="520" width="14" height="130"/>
        <rect x="316" y="470" width="14" height="180"/>
        <rect x="338" y="440" width="14" height="210"/>
        <rect x="360" y="480" width="14" height="170"/>
        <rect x="382" y="420" width="14" height="230"/>
        <rect x="404" y="390" width="14" height="260"/>
        <rect x="426" y="430" width="14" height="220"/>
        <rect x="448" y="370" width="14" height="280"/>
        <rect x="470" y="340" width="14" height="310"/>
      </g>
      <polyline points="0,70 40,120 80,95 120,190 150,140 190,170 240,130 280,220 320,200 360,300 400,270 440,330 480,310"
                fill="none" stroke="rgba(40,80,140,0.3)" stroke-width="3"/>
      <polyline points="250,420 280,380 300,430 330,360 360,400 390,330 420,370 440,300 480,320"
                fill="none" stroke="var(--chart-line)" stroke-width="3"/>
    </svg>

    <div class="cover__compass" role="img" aria-label="Faint compass rose decoration"></div>

    <svg class="cover__portrait" viewBox="0 0 480 720" role="img" aria-label="Photograph of the author in a dark suit and pink tie, smiling">
      <defs>
        <linearGradient id="portraitFill" x1="0" y1="0" x2="0" y2="1">
          <stop offset="0" stop-color="var(--skin)"/>
          <stop offset="0.2" stop-color="#c79a7c"/>
          <stop offset="0.3" stop-color="#6e5443"/>
          <stop offset="0.42" stop-color="var(--suit)"/>
          <stop offset="1" stop-color="#2a3246"/>
        </linearGradient>
      </defs>
      <path fill="url(#portraitFill)"
            d="M75 193 C110 193 133 220 135 255 L132 330 L190 360 L203 380 L205 575 L250 590 L250 720 L0 720 L0 350 L20 335 L18 255 C20 220 42 193 75 193 Z"/>
    </svg>

    <h1 class="cover__title">
      <span class="cover__title-lead">Charting</span>
      <span class="cover__title-main">KELMOR</span>
    </h1>

    <p class="cover__tagline">A Boardroom Leader’s Field Guide to Oversight and Endurance</p>

    <div class="cover__author">Martin J Hollis</div>
  </section>
</div>
</body>
</html>
```